Hula-Hoop dance entertainment sales and instruction by spin-wisp needs a business card

I need a 2 sided business card that is square (although this is not an absolute )for my self employed business as an independent artist. my business name is "Spin-Wisp" I teach how to hula-hoop classes, make and sell hula-hoops, provided entertainment at kids birthday parties, community events, corporate events and perform at artistic dance shows.
I would like to see spirals or curved lines in the card, and I would like the card to be seen as fun, spunky, flair and eye catching.

the card could double as a tag to go on the hoops i sell,

Target Market(s)

women age 20 - 50

Industry/Entity Type

Entertainment

Requirements
Must have
• Dena Marwick
www.spinwispdemo.com
555.014.7263
Nice to have
• I would like my image to be on one side of the card. so people can recognize me!

```html
<!DOCTYPE html>
<html lang="en">
<head>
<meta charset="utf-8">
<title>Dena Marwick – Hoop Services Card</title>
<link rel="stylesheet" href="https://fonts.googleapis.com/css2?family=Federant&family=Noto+Sans:wght@400;700&display=swap">
<style>
  :root {
    --card-bg: #9da1d3;
    --ink: #0d0d12;
    --frame: #0d0d12;
  }
  * { box-sizing: border-box; margin: 0; padding: 0; }
  html, body {
    width: 1200px;
    height: 1200px;
    overflow: hidden;
    background: var(--card-bg);
  }
  .card {
    position: relative;
    width: 1200px;
    height: 1200px;
    background: var(--card-bg);
    border: 8px solid var(--frame);
    color: var(--ink);
    font-family: "Noto Sans", Tahoma, sans-serif;
  }
  .card__name {
    position: absolute;
    top: 48px;
    left: 0;
    width: 100%;
    text-align: center;
    font-family: "Federant", serif;
    font-weight: 400;
    font-size: 132px;
    line-height: 1.1;
    letter-spacing: 4px;
  }
  .card__rule {
    position: absolute;
    left: 155px;
    width: 888px;
    height: 4px;
    background: var(--ink);
  }
  .card__rule--top { top: 256px; }
  .card__rule--bottom { top: 922px; }
  .services {
    position: absolute;
    top: 296px;
    left: 0;
    width: 100%;
    list-style: none;
    text-align: center;
    font-size: 49px;
    line-height: 66px;
    font-weight: 400;
  }
  .contact {
    position: absolute;
    top: 962px;
    left: 0;
    width: 100%;
    text-align: center;
    font-weight: 700;
    font-size: 60px;
    line-height: 78px;
  }
</style>
</head>
<body>
  <main class="card">
    <h1 class="card__name">Dena Marwick</h1>
    <div class="card__rule card__rule--top"></div>
    <ul class="services">
      <li>Hoop Classes</li>
      <li>Hoop Jams</li>
      <li>Private Lessons</li>
      <li>Custom hula-hoops for adults and kids</li>
      <li>Performances</li>
      <li>Hoop Making Workshops</li>
      <li>Birthday Parties</li>
      <li>Corporate Event Entertainment</li>
      <li>and more!</li>
    </ul>
    <div class="card__rule card__rule--bottom"></div>
    <div class="contact">
      <p class="contact__web">www.spinwispdemo.com</p>
      <p class="contact__phone">555.014.7263</p>
    </div>
  </main>
</body>
</html>
```